Heavy Equipment Rental Company Looking for Attractive Sign Design

We need a new sign for our forklift rental company in Southern California called Ridgeline Lift Outfitters. We also sell, service and move forklifts and other equipment, but forklift rentals are our main business. Our old sign on the street is deteriorating quickly. I've attached a photo of the old sign - it is approximately 52" high and 48" wide, but may be made 6" or so taller if needed. The old sign is included more to reference the information than the design - the old design definitely has issues (no ArtMarketry at the time). The smaller sign reading Pellworth dealer is not needed. We want the sign to be simple, clean and easy to read, but of course also attractive and professional. We would like the same information on it as is on the previous sign, but it may be re-arranged. The number 3100 is the street number. Here are the essential elements:
3100 (street number)
Ridgeline Lift Outfitters (business name)
714-382-6047 (phone)
www.ridgelineliftco.example (website)
Forklift Rentals and Sales (main businesses)
If possible, we would like the names of our 2 primary brands:
Pellworth and Varnecki Forklifts
Although, if there's no way to implement them nicely, then we can leave them off.

Target Market(s)

Industrial, Construction

Industry/Entity Type

Construction

Colors
0355a3

Requirements
Must have
• Bold, clean, easy to read, with the necessary information.
Nice to have
• Our main machines are all painted blue, so some blue in the design would be nice. In our industry, Pellworth forklifts and Varnecki forklifts are two different brands but have good reputations. It would be nice if we can include them in the design, although a nice design is more important than including the brand names.
Should not have
• Small or difficult to read text. Colors or fonts that are too playful.

```html
<!DOCTYPE html>
<html lang="en">
<head>
<meta charset="utf-8">
<title>Ridgeline Lift Outfitters – Street Sign</title>
<link rel="stylesheet" href="https://fonts.googleapis.com/css2?family=Bebas+Neue&family=Roboto+Condensed:wght@400;500;700&display=swap">
<style>
  :root {
    --backdrop: #8c8c8c;
    --sign-face: #eceeed;
    --brand-blue: #26479b;
    --on-blue: #ffffff;
  }
  html, body {
    margin: 0;
    width: 1200px;
    height: 970px;
    overflow: hidden;
    background: var(--backdrop);
  }
  .sign {
    position: absolute;
    left: 302px;
    top: 113px;
    width: 596px;
    height: 743px;
    display: block;
  }
  .sign-face { fill: var(--sign-face); }
  .frame-line { fill: none; stroke: var(--brand-blue); stroke-width: 3.5; stroke-linecap: round; stroke-linejoin: round; }
  .display-text { font-family: "Bebas Neue", "Arial Narrow", sans-serif; fill: var(--brand-blue); }
  .body-text { font-family: "Roboto Condensed", "Arial Narrow", sans-serif; fill: var(--brand-blue); }
  .street-number { font-family: "Roboto Condensed", "Arial Narrow", sans-serif; font-weight: 700; font-size: 54px; fill: var(--brand-blue); }
  .service-band { fill: var(--brand-blue); }
  .band-text { font-family: "Roboto Condensed", "Arial Narrow", sans-serif; font-size: 36px; fill: var(--on-blue); }
  .phone { font-weight: 500; font-size: 68px; }
  .web-address { font-size: 35px; }
  .brand-name { font-family: "Roboto Condensed", "Arial Narrow", sans-serif; font-weight: 700; font-size: 42px; fill: var(--brand-blue); }
  .icon-slot { fill: var(--brand-blue); opacity: 0.18; }
</style>
</head>
<body>
<svg class="sign" viewBox="0 0 596 743" xmlns="http://www.w3.org/2000/svg" role="group" aria-label="Ridgeline Lift Outfitters street sign">
  <rect class="sign-face" x="0" y="0" width="596" height="743"/>

  <!-- street number header -->
  <path class="frame-line" d="M21 113 V61 a8 8 0 0 1 8 -8 H208 M386 53 H566 a8 8 0 0 1 8 8 V113"/>
  <rect class="frame-line" x="208" y="22" width="178" height="63" rx="6"/>
  <text class="street-number" x="297" y="75" text-anchor="middle">3100</text>

  <!-- business name -->
  <text class="display-text" x="297" y="187" text-anchor="middle" font-size="92" textLength="375" lengthAdjust="spacingAndGlyphs">RIDGELINE</text>
  <text class="display-text" x="297" y="316" text-anchor="middle" font-size="140" textLength="300" lengthAdjust="spacing">LIFT</text>
  <path class="frame-line" d="M88 239 V325 H255 M341 325 H506 V239"/>

  <rect class="icon-slot" x="14" y="255" width="69" height="74" rx="6" role="img" aria-label="Forklift icon facing right"/>
  <rect class="icon-slot" x="513" y="255" width="69" height="74" rx="6" role="img" aria-label="Forklift icon facing left"/>

  <text class="display-text" x="112" y="407" font-size="82" textLength="375" lengthAdjust="spacing">OUTFITTERS</text>

  <!-- contact panel -->
  <path class="frame-line" d="M21 415 V713 a10 10 0 0 0 10 10 H564 a10 10 0 0 0 10 -10 V415"/>
  <text class="body-text web-address" x="297" y="462" text-anchor="middle" textLength="445" lengthAdjust="spacingAndGlyphs">www.ridgelineliftco.example</text>

  <rect class="service-band" x="24" y="486" width="547" height="60"/>
  <text class="band-text" x="297" y="529" text-anchor="middle" textLength="514" lengthAdjust="spacingAndGlyphs">FORKLIFT RENTALS AND SALES</text>

  <text class="body-text phone" x="297" y="613" text-anchor="middle" textLength="380" lengthAdjust="spacingAndGlyphs">714-382-6047</text>

  <line class="frame-line" x1="24" y1="642" x2="571" y2="642"/>

  <text class="brand-name" x="165" y="698" text-anchor="middle">PELLWORTH</text>
  <text class="brand-name" x="432" y="698" text-anchor="middle">VARNECKI</text>
</svg>
</body>
</html>
```